Boracay Wedding Invitation Design

Hello, We would like a wedding invitation design for our wedding in Boracay. We would like it somewhat in the form of a boarding pass with beachy fresh colours, possibly a nice Boracay beach in the background Double sided with an envelope design to match. Maybe something simple on the envelope like a nice picture in the bottom left corner of a shell on a beach or something similar.

I would also like on the opposite side of the invite to be an "information sheet" with a matching beach design

The text files for both sides are included and i have also included 2 designs that i thought looked nice and are similar to what we are after.
Updates

Hello, I have updated the brief to be more specific with text files and images to make it easier for you. Thank you :)

Industry/Entity Type

Wedding

Font styles to use
Decorative
Script

Colors
fbee3d
33a6d7
33b8a4
fbf289
85cae6
ffffff

Requirements
Must have
• I would like to have this quote somewhere on the invitation
• This day I will marry my best friend,
• the one I laugh with,
• live for,
• dream with,
• love
• Owen & Marisa
• Request the pleasure of your company to celebrate their wedding
• On Friday the 17th March 2017
• at
• Velora Grand Suites
• Boracay, Philippines
• Ceremony begins at 3.00pm
• RSVP
• Owen 0437291856
• Marisa 0418273940
• by
• 17th Jan 2016
• Dress: Beach Formal
• For the "information sheet"
• There will be a 5% discount on rooms booked at the Velora under the event Owen & Marisa Wedding. The resort has a total of 24 rooms it would be nice if the majority of guests could stay at the resort from the night before until the night after the wedding but if you choose to stay elsewhere on the island there are plenty of other places to stay for cheaper and everything is fairly close as its a small island.
• We have currently blocked room stay for a short period of time so our guests can book rooms. If you choose to do so please email reservations@veloraresorts-example.com. Once rooms become available to the public again, towards the end of Jan, it will be first come first served basis. The resort is very popular so im assuming once this happens the rooms will be booked out.
• If you would like to check out the resort itself the website is www.veloragrand-example.com
• We know its a fair distance to travel but we would really love to see you all there to celebrate and maybe even enjoy a small holiday while your here its a beautiful part of the world.
• If anyone has any questions please feel free to contact Owen on 0437291856
Nice to have
• A nice picture of a Boracay beach in the background would be nice

```html
<!DOCTYPE html>
<html lang="en">
<head>
<meta charset="utf-8">
<title>Owen &amp; Marisa – Boracay Wedding Invitation</title>
<link rel="stylesheet" href="https://fonts.googleapis.com/css2?family=Baloo+2:wght@400;500;600;700&family=Great+Vibes&display=swap">
<style>
  :root {
    --frame-blue: #85cae6;
    --ticket-yellow: #f7f28f;
    --ink: #2a1a0e;
    --cocoa: #3a2314;
    --sky-top: #d6eef9;
    --sky-mid: #9fd6ef;
    --sea: #33b8a4;
    --sea-deep: #39a9d3;
    --sand-light: #fbe7a6;
    --sand: #f5b54a;
    --palm: rgba(86, 160, 62, 0.75);
    --palm-dark: rgba(40, 104, 36, 0.9);
    --page: #ffffff;
  }
  * { margin: 0; padding: 0; box-sizing: border-box; }
  html, body { width: 1200px; height: 1122px; overflow: hidden; background: var(--page); }
  body { position: relative; font-family: "Baloo 2", sans-serif; color: var(--ink); }

  .ticket { position: absolute; left: 23px; width: 1160px; background: var(--frame-blue); }
  .ticket--front { top: 29px; height: 521px; }
  .ticket--info { top: 566px; height: 520px; }

  .panel { position: absolute; background: var(--ticket-yellow); border-radius: 14px; }

  /* front */
  .stub-left { left: 13px; top: 12px; width: 108px; height: 499px; }
  .beach { left: 121px; top: 12px; width: 768px; height: 499px; overflow: hidden; border-radius: 0;
    background: linear-gradient(180deg, var(--sky-top) 0%, var(--sky-mid) 26%, var(--sea-deep) 36%, var(--sea) 44%, #c9ebe0 54%, var(--sand-light) 64%, var(--sand) 82%, #f2c86a 100%); }
  .stub-right { left: 891px; top: 12px; width: 256px; height: 499px; }
  .perforation { position: absolute; top: 12px; height: 499px; border-left: 2px dashed var(--cocoa); }
  .perforation--a { left: 120px; }
  .perforation--b { left: 889px; }

  .palm-shade { position: absolute; top: 0; pointer-events: none; }
  .palm-shade--left { left: 0; width: 300px; height: 260px;
    background: radial-gradient(ellipse 100% 100% at 0% 0%, var(--palm-dark) 0%, var(--palm) 38%, rgba(120,180,90,0.25) 62%, rgba(120,180,90,0) 80%); }
  .palm-shade--right { right: 0; width: 220px; height: 170px;
    background: radial-gradient(ellipse 100% 100% at 100% 0%, var(--palm-dark) 0%, var(--palm) 38%, rgba(120,180,90,0.25) 62%, rgba(120,180,90,0) 80%); }

  .hero { position: absolute; left: 0; top: 0; width: 768px; height: 499px; text-align: center; }
  .vow { position: absolute; left: 0; width: 768px; top: 34px; font-size: 21px; font-weight: 500; line-height: 33px; text-transform: uppercase; color: var(--ink); }
  .couple { position: absolute; left: 0; width: 768px; top: 200px; font-family: "Great Vibes", cursive; font-weight: 400; font-size: 88px; line-height: 1; color: var(--cocoa); white-space: nowrap; }
  .request { position: absolute; left: 0; width: 768px; top: 310px; font-size: 21px; font-weight: 600; line-height: 24px; text-transform: uppercase; }

  .detail { position: absolute; text-align: left; white-space: nowrap; }
  .detail dt { font-size: 16px; text-transform: uppercase; line-height: 20px; }
  .detail dd { font-size: 19.5px; font-weight: 500; line-height: 26px; }
  .detail--date { left: 76px; top: 370px; }
  .detail--venue { left: 76px; top: 430px; }
  .detail--place { left: 434px; top: 370px; }
  .detail--time { left: 434px; top: 430px; }

  .rsvp { position: absolute; left: 0; width: 256px; text-align: center; }
  .rsvp h2 { font-size: 23px; font-weight: 600; margin-top: 30px; line-height: 30px; }
  .rsvp p { font-size: 17px; font-weight: 600; line-height: 22px; margin-top: 14px; }
  .date-badge { position: absolute; left: 54px; top: 197px; width: 152px; height: 150px; background: var(--cocoa); border-radius: 14px; color: var(--ticket-yellow); text-align: center; }
  .date-badge .month { display: block; font-size: 27px; font-weight: 500; line-height: 30px; margin-top: 18px; }
  .date-badge .day { display: block; font-size: 100px; font-weight: 500; line-height: 86px; margin-top: 2px; }
  .dress { position: absolute; left: 0; width: 256px; top: 410px; text-align: center; font-size: 17px; font-weight: 600; line-height: 23px; }

  .flower { position: absolute; width: 56px; height: 56px; background: var(--cocoa); border-radius: 50%; }
  .plane { position: absolute; width: 64px; height: 64px; }
  .vertical-tag { position: absolute; left: 50%; transform: translate(-50%, -50%) rotate(-90deg); display: flex; flex-direction: column; align-items: center; white-space: nowrap; }
  .vertical-tag .script { font-family: "Great Vibes", cursive; font-size: 38px; color: var(--cocoa); line-height: 34px; }
  .vertical-tag .caps { font-size: 17px; font-weight: 700; text-transform: uppercase; line-height: 20px; margin-top: 2px; }

  /* info */
  .info-sheet { left: 13px; top: 12px; width: 1024px; height: 496px; }
  .stub-info { left: 1041px; top: 12px; width: 106px; height: 496px; }
  .perforation--c { left: 1039px; top: 12px; height: 496px; }
  .column { position: absolute; top: 44px; font-size: 19.5px; font-weight: 500; line-height: 24.5px; }
  .column--one { left: 49px; width: 450px; }
  .column--two { left: 539px; width: 450px; }
  .column p + p { margin-top: 36px; }
  .column strong { font-weight: 700; }
  .rule { margin-top: 26px; letter-spacing: 3px; }
  .column .contact { margin-top: 20px; font-size: 17.5px; line-height: 24px; }
</style>
</head>
<body>

<section class="ticket ticket--front">
  <div class="panel stub-left">
    <div class="flower" style="left:26px; top:20px;" role="img" aria-label="Hibiscus flower ornament"></div>
    <div class="vertical-tag" style="top:246px;">
      <span class="script">Owen &amp; Marisa</span>
      <span class="caps">Boarding Pass</span>
    </div>
    <svg class="plane" style="left:22px; top:406px;" viewBox="0 0 24 24" aria-hidden="true"><path fill="#2a1a0e" d="M21 16v-2l-8-5V3.5a1.5 1.5 0 0 0-3 0V9l-8 5v2l8-2.5V19l-2 1.5V22l3.5-1 3.5 1v-1.5L13 19v-5.5z" transform="rotate(90 12 12)"/></svg>
  </div>
  <span class="perforation perforation--a"></span>

  <div class="panel beach" role="img" aria-label="Sunny Boracay beach with turquoise sea, golden sand and palm fronds overhead">
    <div class="palm-shade palm-shade--left"></div>
    <div class="palm-shade palm-shade--right"></div>
    <div class="hero">
      <p class="vow">This day I will marry my best friend,<br>the one I laugh with,<br>live for,<br>dream with,<br>love</p>
      <h1 class="couple">Owen &amp; Marisa</h1>
      <p class="request">Request the pleasure of your company to<br>celebrate their wedding</p>
      <dl class="detail detail--date"><dt>Date:</dt><dd>On Friday the 17th March 2017</dd></dl>
      <dl class="detail detail--venue"><dt>Destination:</dt><dd>at Velora Grand Suites</dd></dl>
      <dl class="detail detail--place"><dt>Location:</dt><dd>Boracay, Philippines</dd></dl>
      <dl class="detail detail--time"><dt>Time:</dt><dd>Ceremony begins at 3.00pm</dd></dl>
    </div>
  </div>
  <span class="perforation perforation--b"></span>

  <div class="panel stub-right">
    <div class="rsvp">
      <h2>RSVP</h2>
      <p>Owen 0437291856<br>Marisa 0418273940<br>by 17th Jan 2016</p>
    </div>
    <div class="date-badge"><span class="month">MAR 2017</span><span class="day">17</span></div>
    <p class="dress">DRESS:<br>Beach Formal</p>
  </div>
</section>

<section class="ticket ticket--info">
  <div class="panel info-sheet">
    <div class="column column--one">
      <p>There will be a 5% discount on rooms booked at the Velora under the event <strong>Owen &amp; Marisa Wedding.</strong> The resort has a total of 24 rooms it would be nice if the majority of guests could stay at the resort from the night before until the night after the wedding but if you choose to stay elsewhere on the island there are plenty of other places to stay for cheaper and everything is fairly close as its a small island.</p>
      <p>We have currently blocked room stay for a short period of time so our guests can book rooms. If you choose to do so please email <strong>reservations@veloraresorts-example.com.</strong> Once rooms become available to the public again, towards the end of Jan, it will be first come first served</p>
    </div>
    <div class="column column--two">
      <p>basis. The resort is very popular so I'm assuming once this happens the rooms will be booked out.</p>
      <p>If you would like to check out the resort itself the website is <strong>www.veloragrand-example.com</strong></p>
      <p>We know its a fair distance to travel but we would really love to see you all there to celebrate and maybe even enjoy a small holiday while your here its a beautiful part of the world.</p>
      <div class="rule">-------</div>
      <p class="contact">If anyone has any questions please feel free to contact Owen on 0437291856</p>
    </div>
  </div>
  <span class="perforation perforation--c"></span>
  <div class="panel stub-info">
    <div class="flower" style="left:25px; top:22px;" role="img" aria-label="Hibiscus flower ornament"></div>
    <div class="vertical-tag" style="top:232px;">
      <span class="script">Owen &amp; Marisa</span>
      <span class="caps">Friday the 17th March 2017</span>
    </div>
    <svg class="plane" style="left:21px; top:408px;" viewBox="0 0 24 24" aria-hidden="true"><path fill="#2a1a0e" d="M21 16v-2l-8-5V3.5a1.5 1.5 0 0 0-3 0V9l-8 5v2l8-2.5V19l-2 1.5V22l3.5-1 3.5 1v-1.5L13 19v-5.5z" transform="rotate(90 12 12)"/></svg>
  </div>
</section>

</body>
</html>
```